We specialize in pizza, pasta and salads and are now offering TAKE & BAKE and GRAB & GO ...

Looking for either a 8.5" x 11" or similar for a instore display. WILL BE ON A SWIVELING HOLDER to catch customers attention.

**THIS IS A DOUBLE SIDED PRINT**

ONE SIDE will consist of WHAT'S FOR DINNER TONIGHT? and the following:
* Take & Bake"
* "Baked Pasta"
* Freshly made in house
* Lasagna
$13.50
- please include attached closeup picture and logo

THE OTHER SIDE will consist of
mini charcutier board.
* snack size charcutier delight *
* Enjoy the flavors of gourmet snacking, all in one convenient box!

PRICE $8.99

Winning design will be commissioned to design labels for "grab and go" for take and bake pasta, charcuterie box, pasta salads, candy etc.

Thank you and please do not hesitate to ask any questions.

www.calderipizza.ca
www.fernloop.ca
Logo to be interchanged as they are affiliated meaning FernLoop is a brand within Calderi pizza.

Target Market(s)

our target market is customers who have already entered our business. This is to upsel

Industry/Entity Type

We are in a self serve enviroment and target business people

Requirements
Must have
• must be clean and catchy. We are located in a professional business community.
Nice to have
• Must be appealing, appetizing and utilize our website colors
Should not have
• should not have any carton drawings and not be cluttered (busy)

```html
<!DOCTYPE html>
<html lang="en">
<head>
<meta charset="utf-8">
<title>Calderi Pizza – What's for Dinner Tonight?</title>
<link href="https://fonts.googleapis.com/css2?family=Alfa+Slab+One&family=Montserrat:wght@400;900&display=swap" rel="stylesheet">
<style>
  :root {
    --band: #0b0b0b;
    --ink: #000000;
    --outline: #ffffff;
    --photo-amber: #c9831f;
    --photo-brown: #6e3f12;
    --photo-cream: #efe6d8;
    --photo-gold: #e3a640;
  }
  html, body {
    margin: 0;
    padding: 0;
    width: 927px;
    height: 1200px;
    overflow: hidden;
    background: #ffffff;
  }
  .poster {
    position: relative;
    width: 927px;
    height: 1200px;
    overflow: hidden;
    font-family: "Montserrat", sans-serif;
  }
  .top-band {
    position: absolute;
    left: 0; top: 0;
    width: 927px; height: 44px;
    background: var(--band);
  }
  .food-photo {
    position: absolute;
    left: 0; top: 44px;
    width: 927px; height: 1079px;
    background:
      radial-gradient(ellipse 420px 260px at 560px 640px, var(--photo-cream) 0%, rgba(239,230,216,0) 70%),
      radial-gradient(ellipse 300px 300px at 820px 660px, #f4f0ea 0%, rgba(244,240,234,0) 75%),
      radial-gradient(ellipse 600px 260px at 500px 1000px, var(--photo-amber) 0%, rgba(201,131,31,0) 80%),
      radial-gradient(ellipse 500px 300px at 600px 120px, var(--photo-gold) 0%, rgba(227,166,64,0) 80%),
      radial-gradient(ellipse 400px 200px at 520px 420px, var(--photo-brown) 0%, rgba(110,63,18,0) 80%),
      linear-gradient(180deg, #b56f1f 0%, #8a5018 35%, #c8a27a 60%, #b8782c 100%);
  }
  .edge-strip {
    position: absolute;
    left: 0; top: 44px;
    width: 6px; height: 168px;
    background: #3a3a3a;
  }
  .text-layer {
    position: absolute;
    left: 0; top: 0;
    width: 927px; height: 1200px;
  }
  .headline {
    font-family: "Alfa Slab One", serif;
    font-size: 92px;
    fill: var(--ink);
    stroke: var(--outline);
    stroke-width: 8px;
    paint-order: stroke fill;
    stroke-linejoin: round;
  }
  .menu-item {
    font-family: "Montserrat", sans-serif;
    font-weight: 900;
    font-size: 56px;
    fill: var(--ink);
    stroke: var(--outline);
    stroke-width: 7px;
    paint-order: stroke fill;
    stroke-linejoin: round;
  }
  .bullet { fill: var(--ink); stroke: var(--outline); stroke-width: 4px; }
  .price {
    font-family: "Montserrat", sans-serif;
    font-weight: 900;
    fill: var(--ink);
    stroke: var(--outline);
    stroke-width: 5px;
    paint-order: stroke fill;
    stroke-linejoin: round;
    letter-spacing: -3px;
  }
  .price-label {
    font-family: "Montserrat", sans-serif;
    font-weight: 900;
    font-size: 27px;
    fill: var(--ink);
    stroke: var(--outline);
    stroke-width: 4px;
    paint-order: stroke fill;
  }
  .bottom-band {
    position: absolute;
    left: 0; top: 1123px;
    width: 927px; height: 77px;
    background: var(--band);
  }
  .brand-name {
    position: absolute;
    right: 32px; top: 20px;
    margin: 0;
    color: #ffffff;
    font-family: "Montserrat", sans-serif;
    font-weight: 400;
    font-size: 34px;
    letter-spacing: 1px;
    line-height: 1;
  }
</style>
</head>
<body>
<div class="poster">
  <div class="top-band"></div>
  <div class="food-photo" role="img" aria-label="Close-up photo of baked pasta with melted cheese stretching from a fork above a dish"></div>
  <div class="edge-strip"></div>

  <svg class="text-layer" width="927" height="1200" viewBox="0 0 927 1200">
    <text class="headline" transform="translate(159 252) rotate(-10)">What’s for</text>
    <text class="headline" transform="translate(60 406) rotate(-10)">Dinner Tonight?</text>

    <circle class="bullet" cx="101" cy="571" r="11"/>
    <circle class="bullet" cx="101" cy="648" r="11"/>
    <circle class="bullet" cx="101" cy="738" r="11"/>
    <circle class="bullet" cx="101" cy="824" r="11"/>

    <text class="menu-item" transform="translate(143 577) rotate(-11)">Take &amp; Bake</text>
    <text class="menu-item" transform="translate(143 664) rotate(-11)">Baked Pasta</text>
    <text class="menu-item" transform="translate(143 749) rotate(-11)">Freshly made in house</text>
    <text class="menu-item" transform="translate(143 837) rotate(-11)">Lasagna</text>

    <text class="price" x="97" y="988"><tspan font-size="40" dy="-32">$</tspan><tspan font-size="86" dy="32">13.50</tspan></text>
    <text class="price-label" x="183" y="1026">PRICE</text>
  </svg>

  <div class="bottom-band">
    <p class="brand-name">CALDERI PIZZA</p>
  </div>
</div>
</body>
</html>
```